Business Card Design For Marketing Agnecy LVT

Need business card design for marketing agency.

Dorian Pell
President, CEO
1-555-304-2917
dorian@lumenvaletrewards.net
www.LumenValeTrewards.biz

Back Side:
Boost Sales Using Rewards, Incentives & Giveaways
Get A Free Sample Package

Target Market(s)

B2B

Industry/Entity Type

Marketing

Contact Information for Business Card

Dorian Pell
President, CEO
1-555-304-2917

Back Side:
Get A Free Sample Package

Please note that my current url is OLD DESIGN. I am working on new design and want the business card to match color themes at least on new site. Here is the demo link for new site so you can see the colors I use, etc.

http://pagekilnstudio.example/qx/dorian/lvt_final/index.html

Requirements
Must have
• Please note that my current url is OLD DESIGN. I am working on new design and want the business card to match color themes at least on new site. Here is the demo link for new site so you can see the colors I use, etc.

Nice to have

Should not have

```html
<!DOCTYPE html>
<html lang="en">
<head>
<meta charset="utf-8">
<title>LVT Stationery</title>
<link href="https://fonts.googleapis.com/css2?family=Arimo:wght@400;700&family=Josefin+Sans:wght@400;600&family=Montserrat:wght@700&family=Oswald:wght@400;500&display=swap" rel="stylesheet">
<style>
:root{
  --bg:#d9d9d9;
  --paper:#e6e6e6;
  --blue:#1a68ad;
  --green:#44a047;
  --charcoal:#4a4b4d;
  --ink:#111;
  --muted:#7a7a7a;
  --white:#fff;
}
*{margin:0;padding:0;box-sizing:border-box}
html,body{width:1200px;height:891px;overflow:hidden;background:var(--bg)}
.stage{position:relative;width:1200px;height:891px}

.letterhead{position:absolute;left:52px;top:74px;width:579px;height:741px;background:var(--paper);overflow:hidden;font-family:Arimo,Arial,sans-serif}
.sweep{position:absolute;left:0;top:0;width:100%;height:100%}
.brand{position:absolute;display:flex;align-items:center;gap:6px;font-family:Montserrat,sans-serif;font-weight:700;color:var(--blue);line-height:1.05}
.brand-dot{width:9px;height:9px;border-radius:50%;background:var(--blue);flex:none}
.letterhead .brand{left:26px;top:48px;font-size:17px;width:150px}
.field{position:absolute;font-size:9px;color:var(--muted)}
.field b{display:block;color:var(--ink);font-size:9.5px;margin-bottom:2px}
.subject{left:175px;top:180px}
.date{left:481px;top:178px}
.salutation{position:absolute;left:175px;top:255px;font-size:12px;color:var(--muted)}
.body-copy{position:absolute;left:175px;top:280px;width:354px;font-size:8.75px;line-height:12.35px;color:var(--muted);text-align:justify}
.body-copy p{margin-bottom:12.3px}
.aside{position:absolute;left:40px;top:313px;width:91px;text-align:right;font-size:9px;line-height:12.3px;color:var(--muted)}
.aside p{margin-bottom:7px}
.aside .lead{color:var(--ink)}
.signature{position:absolute;left:175px;top:548px;font-size:12px;line-height:15px;color:var(--muted);font-weight:700}
.contacts{position:absolute;right:20px;font-family:"Josefin Sans",sans-serif;color:var(--white);text-align:right}
.contacts li{list-style:none;display:flex;justify-content:flex-end;align-items:center;gap:7px}
.icon{width:9px;height:9px;border-radius:50%;background:var(--white);display:inline-block;flex:none}
.letterhead .contacts{top:688px;font-size:8.5px;line-height:13px}

.card{position:absolute;left:681px;width:452px;height:262px;border-radius:24px;background:var(--paper);overflow:hidden}
.card-front{top:156px}
.card-back{top:470px}
.card-front .brand{left:16px;top:48px;font-size:26px;width:210px}
.card-front .brand-dot{width:12px;height:12px}
.person{position:absolute;left:16px;top:212px;font-family:"Josefin Sans",sans-serif;color:var(--white)}
.person-name{font-size:16px;font-weight:600;letter-spacing:.3px}
.person-role{font-size:11.5px;margin-top:3px}
.card-front .contacts{top:198px;right:16px;font-size:11px;line-height:17px}
.card-front .icon{width:11px;height:11px}

.card-back .brand{left:0;right:0;top:36px;justify-content:center;font-size:20px}
.tagline{position:absolute;left:0;right:0;top:89px;text-align:center;font-family:Oswald,sans-serif;font-size:14px;font-weight:500;color:var(--charcoal)}
.tagline .boost{color:var(--green);font-size:18px}
.tagline .give{color:var(--blue);font-size:18px}
.band{position:absolute;left:0;top:141px;width:100%;height:121px;background:var(--blue);border-top:12px solid var(--green)}
.offer{position:absolute;left:50%;top:150px;transform:translateX(-50%);width:236px;height:40px;background:var(--green);display:flex;align-items:center;justify-content:center;font-family:Oswald,sans-serif;font-size:17px;font-weight:500;color:var(--white)}
.url{position:absolute;left:0;right:0;top:220px;text-align:center;font-family:Oswald,sans-serif;font-size:14px;color:var(--white)}
</style>
</head>
<body>
<div class="stage">

  <section class="letterhead">
    <svg class="sweep" viewBox="0 0 579 741" preserveAspectRatio="none" role="img" aria-label="Curved footer band in charcoal, green and blue tones">
      <defs>
        <linearGradient id="sweepTone" x1="0" y1="0" x2="0" y2="1">
          <stop offset="0" stop-color="var(--charcoal)"/>
          <stop offset="0.35" stop-color="var(--green)"/>
          <stop offset="0.6" stop-color="var(--blue)"/>
        </linearGradient>
      </defs>
      <path d="M0 680 C200 732 430 662 579 500 V741 H0Z" fill="url(#sweepTone)"/>
    </svg>

    <div class="brand"><span class="brand-dot"></span>Lumen Vale Trewards</div>

    <div class="field subject"><b>SUBJECT :</b>Lorem Ipsum is simply dummy</div>
    <div class="field date"><b>DATE :</b>15-09-2017</div>

    <div class="aside">
      <p class="lead">Lorem Ipsum is<br>simply dummy text<br>of the printing</p>
      <p><span class="lead">Lorem Ipsum is</span><br>simply dummy text</p>
    </div>

    <div class="salutation">Dear Person,</div>
    <div class="body-copy">
      <p>Lorem Ipsum is simply dummy text of the printing and typesetting industry. Lorem Ipsum has been the industry's standard dummy text ever since the 1500s, when an unknown printer took a galley of type and scrambled it to make a type specimen book. It has survived not only five centuries, but also the leap into electronic typesetting, remaining essentially unchanged. It was popularised in the 1960s with the release of Typeleaf sheets containing Lorem Ipsum passages, and more recently with desktop publishing software like Quarto Layout including versions of Lorem Ipsum.</p>
      <p>Lorem Ipsum is simply dummy text of the printing and typesetting industry. Lorem Ipsum has been the industry's standard dummy text ever since the 1500s, when an unknown printer took a galley of type and scrambled it to make a type specimen book. It has survived not only five centuries, but also the leap into electronic typesetting, remaining essentially unchanged. It was popularised in the 1960s with the release of</p>
      <p>Typeleaf sheets containing Lorem Ipsum passages, and more recently with desktop publishing software like Quarto Layout including versions of Lorem Ipsum.lease of Typeleaf sheets containing Lorem Ipsum passages, and more recently with desktop publishing software like Quarto Layout including versions of Lorem Ipsum. publishing software like Quarto Layout including versions of Lorem Ipsum.</p>
    </div>

    <div class="signature">Marlow Keane<br>Managing Director</div>

    <ul class="contacts">
      <li>1-555-304-2917 <span class="icon"></span></li>
      <li>dorian@lumenvaletrewards.net <span class="icon"></span></li>
      <li>www.LumenValeTrewards.biz <span class="icon"></span></li>
    </ul>
  </section>

  <section class="card card-front">
    <svg class="sweep" viewBox="0 0 452 262" preserveAspectRatio="none" role="img" aria-label="Curved lower band in charcoal, green and blue tones">
      <defs>
        <linearGradient id="cardTone" x1="0" y1="0" x2="0" y2="1">
          <stop offset="0" stop-color="var(--charcoal)"/>
          <stop offset="0.3" stop-color="var(--green)"/>
          <stop offset="0.55" stop-color="var(--blue)"/>
        </linearGradient>
      </defs>
      <path d="M0 158 C150 200 330 175 452 8 V262 H0Z" fill="url(#cardTone)"/>
    </svg>
    <div class="brand"><span class="brand-dot"></span>Lumen Vale Trewards</div>
    <div class="person">
      <div class="person-name">Dorian Pell</div>
      <div class="person-role">President, CEO</div>
    </div>
    <ul class="contacts">
      <li>1-555-304-2917 <span class="icon"></span></li>
      <li>dorian@lumenvaletrewards.net <span class="icon"></span></li>
      <li>www.LumenValeTrewards.biz <span class="icon"></span></li>
    </ul>
  </section>

  <section class="card card-back">
    <div class="brand"><span class="brand-dot"></span>Lumen Vale Trewards</div>
    <div class="tagline"><span class="boost">BOOST</span> SALES USING REWARDS, INCENTIVES &amp; <span class="give">GIVEAWAYS</span></div>
    <div class="band"></div>
    <div class="offer">GET A FREE SAMPLE PACKAGE</div>
    <div class="url">WWW.LUMENVALETREWARDS.BIZ</div>
  </section>

</div>
</body>
</html>
```